Business Card Design - Law Firm

I need a business card design. I have attached a picture of the law firm's website and logo. The business card design should be consistent with those pictures. There should be a place for the employee name, employee job title, telephone number, facsimile number, address, website url, and email address for each employee.
Industry/Entity Type
Business

```html
<!DOCTYPE html>
<html lang="en">
<head>
<meta charset="utf-8">
<title>Marlowe Law – Business Card</title>
<link rel="stylesheet" href="https://fonts.googleapis.com/css2?family=Arimo:wght@400;700&family=Marcellus&display=swap">
<style>
  :root {
    --backdrop: #e6e3de;
    --card-white: #ffffff;
    --ink: #333333;
    --ink-dark: #1f1d1c;
    --gold: #a38c46;
    --gold-light: #d9be72;
    --gold-mid: #c3a358;
    --gold-deep: #b49449;
    --band-dark: #1e1c1b;
    --mark: #262321;
  }
  * { box-sizing: border-box; margin: 0; padding: 0; }
  html, body { width: 1186px; height: 1200px; overflow: hidden; }
  body { background: var(--backdrop); position: relative; font-family: "Arimo", Arial, sans-serif; }

  .card { position: absolute; left: 152px; width: 896px; height: 512px; overflow: hidden;
          box-shadow: 0 6px 18px rgba(0,0,0,.18); }

  /* Front */
  .card--front { top: 60px; background: var(--card-white); }
  .card--front .brand { position: absolute; top: 110px; left: 0; right: 0;
          display: flex; align-items: center; justify-content: center; gap: 24px; }
  .brand__square { width: 78px; height: 78px; background: var(--mark); }
  .brand__name { font-family: "Marcellus", Georgia, serif; font-size: 62px; line-height: 1; color: var(--gold); }

  .person { position: absolute; left: 59px; top: 302px; }
  .person__name { font-weight: 700; font-size: 33px; color: var(--gold); letter-spacing: -0.3px; }
  .person__title { font-size: 23px; color: var(--ink); margin-top: 8px; }

  .divider { position: absolute; left: 362px; top: 270px; width: 2px; height: 140px; background: var(--ink); }

  .contact { position: absolute; left: 397px; top: 268px; list-style: none;
             font-size: 25px; line-height: 37px; color: var(--ink); }

  .bands { position: absolute; left: 0; right: 0; bottom: 0; }
  .card--front .bands .band--dark { height: 11px; background: var(--band-dark); }
  .card--front .bands .band--gold { height: 14px; background: var(--gold-mid); }

  /* Back */
  .card--back { top: 624px;
    background: linear-gradient(180deg, var(--gold-light) 0%, var(--gold-mid) 30%, var(--gold-deep) 55%, var(--gold-mid) 80%, var(--gold-light) 100%); }
  .card--back .brand { position: absolute; top: 70px; left: 0; right: 0;
          display: flex; flex-direction: column; align-items: center; gap: 42px; }
  .card--back .brand__square { width: 150px; height: 150px; }
  .card--back .brand__name { color: #ffffff; font-size: 72px; }
  .back-web { position: absolute; left: 0; right: 0; top: 440px; text-align: center;
              font-size: 25px; color: var(--ink-dark); }
  .card--back .bands .band--white { height: 9px; background: #ffffff; }
  .card--back .bands .band--dark { height: 20px; background: var(--band-dark); }
</style>
</head>
<body>
  <section class="card card--front">
    <div class="brand">
      <span class="brand__square"></span>
      <span class="brand__name">Marlowe Law</span>
    </div>
    <div class="person">
      <p class="person__name">Dana Whitfield</p>
      <p class="person__title">CEO</p>
    </div>
    <span class="divider"></span>
    <ul class="contact">
      <li>dana@marlowelaw.com</li>
      <li>www.marlowelaw.com</li>
      <li>Phone 0400 555 018</li>
      <li>Fax 0400 555 018</li>
      <li>PO Box 112, Kelso, NT 0800</li>
    </ul>
    <div class="bands">
      <div class="band--dark"></div>
      <div class="band--gold"></div>
    </div>
  </section>

  <section class="card card--back">
    <div class="brand">
      <span class="brand__square"></span>
      <span class="brand__name">Marlowe Law</span>
    </div>
    <p class="back-web">www.marlowelaw.com</p>
    <div class="bands">
      <div class="band--white"></div>
      <div class="band--dark"></div>
    </div>
  </section>
</body>
</html>
```